Commercial Construction Company

We need a business card design based on our current logo. We are a commercial general contractor based in Southern California that specializes in bank remodels. We would like to see designs that incorporate dark blue. The final design should portray an image of professionalism and quality.

If possible, I would like to add metallic foil to the design. Thank you

```html
<!DOCTYPE html>
<html lang="en">
<head>
<meta charset="utf-8">
<title>Harlow Commercial Building Group – Business Card</title>
<link href="https://fonts.googleapis.com/css2?family=Lato:wght@400;700&display=swap" rel="stylesheet">
<style>
  :root {
    --brand-blue: #0f4a85;
    --accent-grey: #a7a9ac;
    --ink: #222222;
    --paper: #ffffff;
    --backdrop: #e9e6e1;
  }
  html, body {
    margin: 0;
    padding: 0;
    width: 1200px;
    height: 900px;
    overflow: hidden;
    background: var(--backdrop);
    font-family: "Lato", sans-serif;
  }
  .canvas {
    position: relative;
    width: 1200px;
    height: 900px;
  }
  .card {
    position: absolute;
    width: 560px;
    height: 320px;
    box-shadow: 0 10px 28px rgba(0,0,0,0.22);
    overflow: hidden;
  }
  .card--back {
    left: 120px;
    top: 150px;
    background: var(--brand-blue);
    display: flex;
    align-items: center;
    justify-content: center;
  }
  .card--front {
    left: 520px;
    top: 430px;
    background: var(--paper);
  }
  .brand {
    display: flex;
    align-items: center;
    gap: 14px;
  }
  .brand__dot {
    width: 30px;
    height: 30px;
    border-radius: 50%;
    background: currentColor;
  }
  .brand__name {
    font-weight: 700;
    font-size: 58px;
    letter-spacing: 1px;
    line-height: 1;
  }
  .card--back .brand { color: var(--paper); }
  .card--front .brand {
    position: absolute;
    right: 42px;
    top: 52px;
    color: var(--ink);
  }
  .card--front .brand__name { font-size: 50px; }
  .card--front .brand__dot { width: 24px; height: 24px; }
  .wave {
    position: absolute;
    left: 0;
    top: 0;
    width: 560px;
    height: 320px;
  }
  .holder {
    position: absolute;
    left: 44px;
    top: 58px;
  }
  .holder__name {
    margin: 0;
    color: var(--brand-blue);
    font-weight: 700;
    font-size: 22px;
    letter-spacing: 0.5px;
  }
  .holder__role {
    margin: 2px 0 0;
    color: #444;
    font-size: 16px;
  }
  .contact {
    position: absolute;
    left: 44px;
    top: 140px;
    margin: 0;
    padding: 0;
    list-style: none;
    color: var(--ink);
    font-size: 16px;
    line-height: 22px;
  }
  .contact__item {
    display: flex;
    align-items: center;
    gap: 8px;
  }
  .contact__icon {
    width: 13px;
    height: 13px;
    fill: var(--brand-blue);
    flex: none;
  }
  .contact__address {
    margin-top: 8px;
    line-height: 20px;
  }
</style>
</head>
<body>
<main class="canvas">
  <section class="card card--back" aria-label="Card back">
    <div class="brand">
      <span class="brand__dot"></span>
      <span class="brand__name">HCBG</span>
    </div>
  </section>

  <section class="card card--front" aria-label="Card front">
    <svg class="wave" viewBox="0 0 560 320" preserveAspectRatio="none" aria-hidden="true">
      <path d="M0,290 C200,328 400,278 560,118 L560,320 L0,320 Z" fill="var(--accent-grey)"/>
      <path d="M0,300 C205,338 410,288 560,132 L560,320 L0,320 Z" fill="var(--paper)"/>
      <path d="M0,312 C210,350 415,300 560,144 L560,320 L0,320 Z" fill="var(--brand-blue)"/>
    </svg>

    <div class="brand">
      <span class="brand__dot"></span>
      <span class="brand__name">HCBG</span>
    </div>

    <div class="holder">
      <h1 class="holder__name">DANIEL REYES</h1>
      <p class="holder__role">Managing Director</p>
    </div>

    <ul class="contact">
      <li class="contact__item">
        <svg class="contact__icon" viewBox="0 0 16 16" aria-hidden="true"><path d="M3.6 1.2l2.4 2.6-1.3 1.8c.9 1.9 2.5 3.5 4.6 4.6l1.8-1.3 2.6 2.4-1.4 2.6C7.3 13.6 2.4 8.7 1.1 2.6z"/></svg>
        <span>044-987 654 321</span>
      </li>
      <li class="contact__item">
        <svg class="contact__icon" viewBox="0 0 16 16" aria-hidden="true"><path d="M1 3h14v10H1z M1.5 3.5L8 9l6.5-5.5" stroke="#fff" stroke-width="1"/></svg>
        <span>info@harlowbuild.com</span>
      </li>
      <li class="contact__item">
        <svg class="contact__icon" viewBox="0 0 16 16" aria-hidden="true"><circle cx="8" cy="8" r="7"/><path d="M1 8h14M8 1c-3 3-3 11 0 14M8 1c3 3 3 11 0 14" stroke="#fff" stroke-width="1" fill="none"/></svg>
        <span>www.harlowbuild.com</span>
      </li>
      <li class="contact__address">421, Address line here<br>45452, Country Name</li>
    </ul>
  </section>
</main>
</body>
</html>
```